Website redesign for job agency recruitment

Please refer to the attached document, “Meridian Crew Website Brief,” for comprehensive details regarding the scope, objectives, and requirements of this website redesign project.

For imagery you can use images from this website https://www.pixmeadow.com or any other you regularly use.

Target Market(s)

Jobseekers and Companies looking for general labour

Industry/Entity Type

Services: Oil, Gas and Mining, Administrative, Construction and Trades, Warehouse and Logistics and, Manufacturing.

Number of Pages Required

5+ page

Font styles to use
Serif
Other font styles liked:
• Inter, Open-Sans or similar.

Requirements
Must have
• The requirements highlighted in the Word document attached. The final design needs to be provided in Figma including all viewports (Desktop, mobiel and tablet)
Should not have
• Website we like as a reference: www.bexworthhiringco.com, www.valtrohiring.com, www.zumvex.com, www.pembrookhiring.com, www.7qtalentry.com, www.quillbergroup.ca

```html
<!DOCTYPE html>
<html lang="en">
<head>
<meta charset="utf-8">
<title>Candidate Application Form – Registration Layouts</title>
<link href="https://fonts.googleapis.com/css2?family=Inter:wght@400;500;600;700&family=Barlow+Semi+Condensed:wght@600;700&display=swap" rel="stylesheet">
<style>
:root{
  --stage:#e8e8e8;
  --panel:#f5f6f8;
  --card:#ffffff;
  --field:#f3f4f6;
  --line:#e4e6ea;
  --navy:#0f3b96;
  --navy-dark:#0b2c72;
  --gold:#f2b705;
  --gold-dark:#e0a200;
  --ink:#15171c;
  --muted:#6b7078;
  --radio:#c9ccd2;
}
*{box-sizing:border-box;margin:0;padding:0}
html,body{width:1200px;height:816px;overflow:hidden;background:var(--stage)}
body{position:relative;font-family:"Inter",sans-serif;color:var(--ink)}
.abs{position:absolute}
.layout-heading{position:absolute;font-weight:700;font-size:11.5px;letter-spacing:.3px;color:#111}
.panel{position:absolute;background:var(--panel)}
.photo-fill{position:absolute;background:linear-gradient(160deg,#1d4aa8 0%,#163d92 45%,#0e2f7a 100%)}
.brand{position:absolute;text-align:center;color:#fff;font-family:"Inter",sans-serif;font-weight:600;font-size:8px;letter-spacing:.1px}
.brand .mark{display:block;width:34px;height:34px;border-radius:50%;border:2px solid #fff;margin:0 auto 5px}
.form-title{position:absolute;font-family:"Barlow Semi Condensed",sans-serif;font-weight:700;font-size:15.5px;line-height:19px;color:var(--ink)}
.form-title .hl{background:var(--gold);padding:0 2px}
.form-sub{position:absolute;font-size:5.9px;color:#222}
.tabs{position:absolute;background:var(--card);border:1px solid var(--line);border-radius:3px;overflow:hidden;display:flex}
.tab{display:flex;align-items:center;justify-content:center;gap:7px;font-family:"Barlow Semi Condensed",sans-serif;font-weight:600;font-size:10px;color:var(--ink)}
.tab.active{background:linear-gradient(90deg,var(--navy-dark),var(--navy));color:#fff;justify-content:flex-start;padding-left:14px}
.tab .ico{width:17px;height:17px;border-radius:50%;background:#fff;border:1px solid var(--line)}
.tab.inactive .ico{background:#f1f2f4}
.card{position:absolute;background:var(--card);border:1px solid var(--line);border-radius:6px}
.label{position:absolute;font-size:6px;font-weight:500;color:var(--ink)}
.field{position:absolute;height:25px;background:var(--field);border:1px solid var(--line);border-radius:2px;display:flex;align-items:center;padding-left:8px;gap:6px;font-size:6.4px;color:#555}
.field.filled{color:var(--navy);font-weight:500}
.field svg{width:9px;height:9px;flex:none}
.radio{position:absolute;display:flex;align-items:center;gap:5px;font-size:6.3px;color:var(--muted)}
.radio::before{content:"";width:5.5px;height:5.5px;border-radius:50%;border:.7px solid var(--radio);background:#fff;box-sizing:border-box}
.radio.on{color:var(--navy);font-weight:500}
.radio.on::before{border-color:#d5dbea;background:radial-gradient(circle,var(--navy) 0 1.5px,#fff 1.7px)}
.submit{position:absolute;width:107px;height:22px}
.submit .btn{position:absolute;inset:0;background:linear-gradient(180deg,#f7c20f,var(--gold-dark));clip-path:polygon(0 0,100% 0,92% 100%,0 100%);display:flex;align-items:center;justify-content:center;padding-right:10px;font-family:"Barlow Semi Condensed",sans-serif;font-weight:700;font-size:8.5px;color:#111}
.submit svg{position:absolute;right:1px;bottom:0;width:9px;height:10px}
.clear{position:absolute;font-size:6.3px;color:var(--navy);text-decoration:underline;transform:translateX(-100%)}
</style>
</head>
<body>
<svg width="0" height="0" style="position:absolute">
  <defs>
    <symbol id="i-user" viewBox="0 0 12 12"><circle cx="6" cy="4" r="2.3" fill="none" stroke="#555" stroke-width="1"/><path d="M2 11c0-2.4 1.8-3.6 4-3.6s4 1.2 4 3.6" fill="none" stroke="#555" stroke-width="1"/></symbol>
    <symbol id="i-phone" viewBox="0 0 12 12"><rect x="3" y="1" width="6" height="10" rx="1.3" fill="none" stroke="#555" stroke-width="1"/><path d="M5.2 9.3h1.6" stroke="#555" stroke-width="1"/></symbol>
    <symbol id="i-bag" viewBox="0 0 12 12"><rect x="1" y="3.5" width="10" height="7" rx="1.2" fill="none" stroke="#555" stroke-width="1"/><path d="M4.2 3.5V2h3.6v1.5M1 6.5h10" fill="none" stroke="#555" stroke-width="1"/></symbol>
    <symbol id="i-cal" viewBox="0 0 12 12"><rect x="1" y="2" width="10" height="9" rx="1.3" fill="none" stroke="#555" stroke-width="1"/><path d="M1 5h10M4 1v2M8 1v2" stroke="#555" stroke-width="1"/></symbol>
    <symbol id="i-pin" viewBox="0 0 12 12"><path d="M6 11s4-3.6 4-6.3A4 4 0 0 0 2 4.7C2 7.4 6 11 6 11z" fill="none" stroke="#555" stroke-width="1"/><circle cx="6" cy="4.8" r="1.4" fill="none" stroke="#555" stroke-width="1"/></symbol>
    <symbol id="i-mail" viewBox="0 0 12 12"><rect x="1" y="2.5" width="10" height="7.5" rx="1.2" fill="none" stroke="#555" stroke-width="1"/><path d="M1.5 3.2 6 6.6l4.5-3.4" fill="none" stroke="#555" stroke-width="1"/></symbol>
  </defs>
</svg>

<!-- Registration layout one -->
<div class="layout-heading" style="left:49px;top:66px">REGISTRATION &nbsp;- ONE</div>
<section class="panel" style="left:46px;top:98px;width:531px;height:623px">
  <div class="photo-fill" style="left:0;top:0;width:218px;height:623px" role="img" aria-label="Mosaic of workplace photos: construction workers, oil field pumpjacks and office staff, tinted blue"></div>
  <div class="brand" style="left:0;top:322px;width:218px">
    <span class="mark"></span>MCA · Meridian Crew Agency Ltd.
  </div>
</section>
<h1 class="form-title" style="left:292px;top:120px">Candidate <span class="hl">Application Form</span></h1>
<p class="form-sub" style="left:292px;top:144px">Please select your primary work region and complete all required fields below.</p>
<div class="tabs" style="left:292px;top:160px;width:249px;height:27px">
  <div class="tab active" style="width:120px"><span class="ico"></span>British Columbia</div>
  <div class="tab inactive" style="flex:1"><span class="ico"></span>Alberta</div>
</div>
<div class="card" style="left:292px;top:195px;width:249px;height:494px"></div>

<span class="label" style="left:303px;top:206px">Full Name *</span>
<div class="field filled" style="left:303px;top:217px;width:227px"><svg><use href="#i-user"/></svg>Alex Moore</div>
<span class="label" style="left:303px;top:251px">Phone Number *</span>
<div class="field" style="left:303px;top:262px;width:227px"><svg><use href="#i-phone"/></svg>+97 55501 20384</div>
<span class="label" style="left:303px;top:296px">Job Title *</span>
<div class="field" style="left:303px;top:307px;width:227px"><svg><use href="#i-bag"/></svg>Construction Worker</div>
<span class="label" style="left:303px;top:341px">Availability *</span>
<span class="radio" style="left:303px;top:354px">Full-time</span>
<span class="radio" style="left:417px;top:354px">Part-time</span>
<span class="radio on" style="left:303px;top:368px">On-Call</span>
<span class="radio" style="left:417px;top:368px">Temporary</span>
<span class="label" style="left:303px;top:385px">Transportation *</span>
<span class="radio on" style="left:303px;top:398px">Car</span>
<span class="radio" style="left:417px;top:398px">Transit</span>
<span class="label" style="left:303px;top:416px">Status *</span>
<span class="radio" style="left:303px;top:429px">Citizen</span>
<span class="radio" style="left:417px;top:429px">Permanent Resident</span>
<span class="radio on" style="left:303px;top:443px">Open Work Permit</span>
<span class="radio" style="left:417px;top:443px">Closed Work Permit</span>
<span class="radio" style="left:303px;top:457px">Student</span>
<span class="radio" style="left:417px;top:457px">Visitor</span>
<span class="radio" style="left:303px;top:471px">Other</span>
<span class="label" style="left:303px;top:487px">Date of Birth *</span>
<div class="field" style="left:303px;top:498px;width:227px"><svg><use href="#i-cal"/></svg>dd / mm / yy</div>
<span class="label" style="left:303px;top:532px">Address</span>
<div class="field" style="left:303px;top:543px;width:227px"><svg><use href="#i-pin"/></svg>48 Alder Row, Fernvale, OR 97001</div>
<span class="label" style="left:303px;top:577px">Email</span>
<div class="field" style="left:303px;top:588px;width:227px"><svg><use href="#i-mail"/></svg>alexmoore@inbox.test</div>
<span class="label" style="left:303px;top:622px">Gendar</span>
<span class="radio" style="left:303px;top:633px">Male</span>
<span class="radio on" style="left:379px;top:633px">Female</span>
<span class="radio" style="left:455px;top:633px">Other</span>
<div class="submit" style="left:303px;top:656px"><div class="btn">Submit Form</div><svg viewBox="0 0 9 10"><path d="M9 0v10H0z" fill="#1d4fb8"/></svg></div>
<span class="clear" style="left:530px;top:664px">Clear Form</span>

<!-- Registration layout two -->
<div class="layout-heading" style="left:614px;top:66px">REGISTRATION &nbsp;- TWO</div>
<section class="panel" style="left:614px;top:98px;width:531px;height:645px">
  <div class="photo-fill" style="left:0;top:0;width:531px;height:109px" role="img" aria-label="Banner mosaic of workplace photos: construction crews, oil field equipment and office staff, tinted blue"></div>
  <div class="brand" style="left:0;top:30px;width:531px">
    <span class="mark"></span>MCA · Meridian Crew Agency Ltd.
  </div>
</section>
<h1 class="form-title" style="left:662px;top:222px">Candidate <span class="hl">Application Form</span></h1>
<p class="form-sub" style="left:662px;top:246px">Please select your primary work region and complete all required fields below.</p>
<div class="tabs" style="left:662px;top:261px;width:434px;height:30px">
  <div class="tab active" style="width:213px"><span class="ico"></span>British Columbia</div>
  <div class="tab inactive" style="flex:1"><span class="ico"></span>Alberta</div>
</div>
<div class="card" style="left:662px;top:300px;width:434px;height:413px"></div>

<span class="label" style="left:673px;top:311px">Full Name *</span>
<div class="field filled" style="left:673px;top:323px;width:202px"><svg><use href="#i-user"/></svg>Alex Moore</div>
<span class="label" style="left:884px;top:311px">Phone Number *</span>
<div class="field" style="left:884px;top:323px;width:201px"><svg><use href="#i-phone"/></svg>+97 55501 20384</div>
<span class="label" style="left:673px;top:357px">Job Title *</span>
<div class="field" style="left:673px;top:369px;width:412px"><svg><use href="#i-bag"/></svg>Construction Worker</div>
<span class="label" style="left:673px;top:403px">Availability *</span>
<span class="radio" style="left:673px;top:417px">Full-time</span>
<span class="radio" style="left:880px;top:417px">Part-time</span>
<span class="radio on" style="left:673px;top:431px">On-Call</span>
<span class="radio" style="left:880px;top:431px">Temporary</span>
<span class="label" style="left:673px;top:449px">Transportation *</span>
<span class="radio on" style="left:673px;top:462px">Car</span>
<span class="radio" style="left:880px;top:462px">Transit</span>
<span class="label" style="left:673px;top:481px">Status *</span>
<span class="radio" style="left:673px;top:494px">Citizen</span>
<span class="radio" style="left:880px;top:494px">Permanent Resident</span>
<span class="radio on" style="left:673px;top:508px">Open Work Permit</span>
<span class="radio" style="left:880px;top:508px">Closed Work Permit</span>
<span class="radio" style="left:673px;top:522px">Student</span>
<span class="radio" style="left:880px;top:522px">Visitor</span>
<span class="radio" style="left:673px;top:536px">Other</span>
<span class="label" style="left:673px;top:553px">Date of Birth *</span>
<div class="field" style="left:673px;top:564px;width:202px"><svg><use href="#i-cal"/></svg>dd / mm / yy</div>
<span class="label" style="left:884px;top:553px">Address</span>
<div class="field" style="left:884px;top:564px;width:201px"><svg><use href="#i-pin"/></svg>48 Alder Row, Fernvale, OR 97001</div>
<span class="label" style="left:673px;top:600px">Email</span>
<div class="field" style="left:673px;top:611px;width:412px"><svg><use href="#i-mail"/></svg>alexmoore@inbox.test</div>
<span class="label" style="left:673px;top:646px">Gendar</span>
<span class="radio" style="left:673px;top:656px">Male</span>
<span class="radio on" style="left:811px;top:656px">Female</span>
<span class="radio" style="left:948px;top:656px">Other</span>
<div class="submit" style="left:673px;top:680px"><div class="btn">Submit Form</div><svg viewBox="0 0 9 10"><path d="M9 0v10H0z" fill="#1d4fb8"/></svg></div>
<span class="clear" style="left:1085px;top:688px">Clear Form</span>
</body>
</html>
```